Speciality Coffee Shop
Project: Speciality Coffee Shop
Speciality Coffee Shop - Beverages
Creative Brief
Beverages
We chose the name Vireo because it defines the base of coffee and its beginning however our cafe will be serving unique and innovative new drinks which will allow people with different tastes to enjoy the drink. Please update the attached company profile based on the points discussed in the details.
Tornqel58 Tornqel58
Draft #2 : I understand however can you please add a few more slides an input the extra information i provided in the last comment?
Pelomir Pelomir
Hello thanks for rating and comment. First thing we are not professional content writer we are designer. Text content should be provided. You need to hire professional writer for this purpose. I hope you got my point. What I can do is to add the image as you said. Because that is related to design.
Draft #2 : Great job! You are going in the right direction but please find the comments below: 1. The first image you used looks nice but please add other images related to specialty coffee in other slides (such as a Q45 or Slow Brew) 2. Please do not Copy and Paste the text that i gave but use it as a reference. Feel free to change the text to make it more professional. 3. We need a more information on our company profile. Please find below a list of Q&A's for your refference. You can use some of my answers and put them in the profile. Q&A Q: Where is the coffee from? the origin or country imported from A: Colombia, Ethiopia, Kenya, and Panama Q: What is Specialty Coffee? A: According to the Premium Bean Guild of Norland (PBGN), coffee which scores 80 points or above on a 100-point scale is graded "specialty." Specialty coffees are grown in special and ideal climates, and are distinctive because of their full cup taste and little to no defects. In general, we will only select our coffee from suppliers that are certified to be specialty coffee suppliers. Q: Taste A: Each coffee bean tastes different. Some have an after taste of nuts and other have a flowery taste and many more tastes. Weather our customers like their coffee strong (such as an espresso) or sweet (such as our unique Lattes) we will cater to all needs. Q: Short brief on each investor. A: We do not require a brief on each investor individually. The 4 investors Tarek Bensouda, Yousef Qandil, Omar Zaytouni and Hamza Raddaoui have been friends since college. We always had a passion for coffee and were continuously looking for great coffee shops around the country as well as abroad. We finally decided to open our own specialty coffee to ensure that people can trust that it is a specialty coffee shop built by passion rather than financial goals. Q: What are your value propositions or unique selling propositions? A: We will only serve the world's finest specialty coffee, independently tested and scored by certified graders. All our baristas will be certified in the entire aspects of coffee. They will have knowledge from bean to cup to unique latte art. Quality is our number 1 goal. We will never reduce the quality of our items no matter what. Q: What are your vision & mission Our vision is to be the world benchmark for quality coffee. (Please try to think of something better) Our mission is to gather people together over a cup of coffee. (Please try to think of something better.

```html
<!DOCTYPE html>
<html lang="en">
<head>
<meta charset="utf-8">
<title>Vireo Coffee – Design Concept</title>
<link rel="stylesheet" href="https://fonts.googleapis.com/css2?family=Montserrat:wght@400;500;700&display=swap">
<style>
  :root {
    --wall-light: #7a5532;
    --wall-dark: #2c1a0e;
    --table-light: #6b4326;
    --table-dark: #24140a;
    --grinder-light: #b88a5c;
    --grinder-mid: #8a5c36;
    --grinder-dark: #4a2c17;
    --cream: #ffffff;
    --note-panel: rgba(24, 13, 6, 0.62);
    --portrait-fill: #ffffff;
    --portrait-ring: #24140a;
  }
  * { margin: 0; padding: 0; box-sizing: border-box; }
  html, body {
    width: 1200px;
    height: 850px;
    overflow: hidden;
    background: var(--wall-dark);
  }
  .profile-page {
    position: relative;
    width: 1200px;
    height: 850px;
    overflow: hidden;
    font-family: "Montserrat", sans-serif;
    color: var(--cream);
  }
  .wall {
    position: absolute;
    left: 0; top: 0;
    width: 1200px; height: 500px;
    background: radial-gradient(ellipse 760px 460px at 880px 160px, var(--wall-light), var(--wall-dark) 85%);
  }
  .table-top {
    position: absolute;
    left: 0; top: 480px;
    width: 1200px; height: 370px;
    background: linear-gradient(180deg, var(--table-light) 0%, var(--table-dark) 100%);
  }
  .grinder-photo {
    position: absolute;
    left: 596px; top: 48px;
    width: 540px; height: 660px;
    border-radius: 120px 120px 24px 24px;
    background: linear-gradient(160deg, var(--grinder-light) 0%, var(--grinder-mid) 45%, var(--grinder-dark) 100%);
  }
  .brand-name {
    position: absolute;
    left: 46px;
    top: 62px;
    font-size: 92px;
    font-weight: 500;
    letter-spacing: 24px;
    line-height: 1;
  }
  .design-concept {
    position: absolute;
    left: 48px;
    top: 252px;
    width: 500px;
  }
  .design-concept h2 {
    font-size: 26px;
    font-weight: 700;
    margin-bottom: 16px;
  }
  .design-concept p {
    font-size: 25px;
    font-weight: 400;
    line-height: 43px;
  }
  .investors {
    position: absolute;
    left: 36px;
    top: 570px;
  }
  .investors h2 {
    font-size: 29px;
    font-weight: 700;
    margin-bottom: 20px;
  }
  .investor-list {
    display: flex;
    gap: 36px;
    list-style: none;
  }
  .investor {
    width: 138px;
    text-align: center;
  }
  .investor-portrait {
    width: 138px;
    height: 138px;
    border-radius: 50%;
    background: var(--portrait-fill);
    border: 4px solid var(--portrait-ring);
  }
  .investor-name {
    margin-top: 18px;
    font-size: 14px;
    font-weight: 700;
    line-height: 17px;
  }
  .note-panel {
    position: absolute;
    left: 730px;
    top: 612px;
    width: 470px;
    height: 238px;
    background: var(--note-panel);
    padding: 10px 18px 0 10px;
    text-align: right;
  }
  .note-panel h3 {
    font-size: 15px;
    font-weight: 700;
    margin-bottom: 8px;
  }
  .note-panel p {
    font-size: 16px;
    line-height: 29px;
    font-weight: 400;
  }
</style>
</head>
<body>
  <main class="profile-page">
    <div class="wall" role="img" aria-label="Warm brown blurred café wall behind the grinder"></div>
    <div class="table-top" role="img" aria-label="Rustic wooden table scattered with roasted coffee beans"></div>
    <div class="grinder-photo" role="img" aria-label="Photograph of a carved wooden manual coffee grinder with a crank handle and an open drawer full of roasted beans"></div>

    <h1 class="brand-name">VIREO</h1>

    <section class="design-concept">
      <h2>Design Concept</h2>
      <p>The interior design of Vireo! Coffee would have a modern and elegant look. However, paintings similar to the ones below would be a nice twist.</p>
    </section>

    <section class="investors">
      <h2>Investors</h2>
      <ul class="investor-list">
        <li class="investor">
          <div class="investor-portrait"></div>
          <p class="investor-name">Tarek<br>Bensouda</p>
        </li>
        <li class="investor">
          <div class="investor-portrait"></div>
          <p class="investor-name">Hamza<br>Raddaoui</p>
        </li>
        <li class="investor">
          <div class="investor-portrait"></div>
          <p class="investor-name">Yousef<br>Qandil</p>
        </li>
        <li class="investor">
          <div class="investor-portrait"></div>
          <p class="investor-name">Omar<br>Zaytouni</p>
        </li>
      </ul>
    </section>

    <aside class="note-panel">
      <h3>Note</h3>
      <p>Thank you for reading our company profile. Please<br>note that we are currently working with interior<br>designers, coffee consultants and food consultants to<br>ensure that we stand out of the crowd. More<br>information will be shared with you soon.</p>
    </aside>
  </main>
</body>
</html>
```